Business Card Design Project

We need a business card design for a new boutique consulting company, TivaConsulting. Our new logo has just been designed and we are looking for simple, clean looking business cards. Logo attached

Industry/Entity Type

Boutique

Requirements
Must have
• There must be room for each card to have the following details:
Name
Title
Address - 2 lines
Phone number
Email address
Website address

Nice to have
• May have something on the back of the buisness card - emphasing the word "Tiva".

```html
<!DOCTYPE html>
<html lang="en">
<head>
<meta charset="utf-8">
<title>TivaConsulting Business Cards</title>
<link href="https://fonts.googleapis.com/css2?family=Questrial&family=Didact+Gothic&family=Mulish:wght@800&display=swap" rel="stylesheet">
<style>
  :root {
    --page-top: #ffffff;
    --page-bottom: #d9d9d9;
    --green-light: #a6d640;
    --green: #6cc04a;
    --green-deep: #4bb43f;
    --silver-light: #f7f8f9;
    --silver: #dfe1e4;
    --ink-grey: #8a8d90;
    --ink-soft: #9c9fa2;
    --white: #ffffff;
  }
  * { margin: 0; padding: 0; box-sizing: border-box; }
  html, body { width: 1200px; height: 1200px; overflow: hidden; }
  body {
    background: radial-gradient(circle at 50% 45%, var(--page-top) 0%, #f1f1f1 55%, var(--page-bottom) 100%);
    position: relative;
    font-family: "Didact Gothic", sans-serif;
  }
  .card {
    position: absolute;
    width: 860px;
    height: 491px;
    overflow: hidden;
    box-shadow: 0 14px 30px rgba(0,0,0,0.22);
  }

  /* Front */
  .card-front {
    left: 70px; top: 80px;
    background: linear-gradient(115deg, var(--silver) 0%, var(--silver-light) 40%, var(--silver) 75%, #eceef0 100%);
  }
  .band {
    position: absolute; left: 0; width: 100%; height: 44px;
    background: linear-gradient(90deg, var(--green-deep) 0%, var(--green) 45%, var(--green-light) 80%, var(--green) 100%);
  }
  .band-top { top: 0; }
  .band-bottom { bottom: 0; }
  .watermark-name {
    position: absolute; left: 20px; top: 110px;
    font-family: "Questrial", sans-serif;
    font-size: 250px; line-height: 1;
    color: rgba(255,255,255,0.7);
    letter-spacing: -6px;
  }
  .wordmark {
    position: absolute; left: 235px; top: 148px;
    font-family: "Questrial", sans-serif;
    font-size: 84px; line-height: 1;
    color: var(--green);
    letter-spacing: -1px;
  }
  .person {
    position: absolute; left: 245px; top: 338px; text-align: right; width: 270px;
  }
  .person-name {
    font-family: "Mulish", sans-serif; font-weight: 800;
    font-size: 22px; color: var(--green); letter-spacing: 0.5px;
  }
  .person-title { font-size: 15px; color: var(--ink-grey); margin-top: 2px; }
  .contact {
    position: absolute; left: 545px; top: 300px;
    font-size: 15px; color: var(--ink-soft); line-height: 22px;
    list-style: none;
  }
  .contact li { display: flex; align-items: center; gap: 6px; }
  .contact svg { width: 15px; height: 15px; flex: none; }

  /* Back */
  .card-back {
    left: 270px; top: 650px;
    background:
      linear-gradient(100deg, rgba(255,255,255,0) 0%, rgba(255,255,255,0.12) 30%, rgba(255,255,255,0) 50%, rgba(255,255,255,0.1) 70%, rgba(255,255,255,0) 100%),
      radial-gradient(ellipse at 55% 35%, var(--green-light) 0%, var(--green) 55%, var(--green-deep) 100%);
  }
  .back-name {
    position: absolute; left: 250px; top: 85px;
    font-family: "Questrial", sans-serif; color: var(--white);
    font-size: 210px; line-height: 1; letter-spacing: -4px;
  }
  .back-sub {
    position: absolute; left: 470px; top: 300px;
    font-family: "Questrial", sans-serif; color: var(--white);
    font-size: 64px; line-height: 1;
  }
</style>
</head>
<body>

<section class="card card-front" aria-label="Business card front">
  <div class="band band-top"></div>
  <div class="band band-bottom"></div>
  <div class="watermark-name" aria-hidden="true">tiva</div>
  <div class="wordmark">TivaConsulting</div>

  <div class="person">
    <p class="person-name">CONSULTANT NAME</p>
    <p class="person-title">Tiva Consultant</p>
  </div>

  <ul class="contact">
    <li>PO Box 48120</li>
    <li>Nelson 7010 New Zealand</li>
    <li>
      <svg viewBox="0 0 16 16" aria-hidden="true"><path d="M4 1.5l2.2 2.8-1.3 1.6c.9 2 2.4 3.5 4.4 4.4l1.6-1.3 2.8 2.2-1.4 2.3C7.5 13.2 2.8 8.5 1.7 3z" fill="var(--green)"/></svg>
      + 64 20 555 0142
    </li>
    <li>
      <svg viewBox="0 0 16 16" aria-hidden="true"><rect x="1.5" y="3.5" width="13" height="9" fill="none" stroke="var(--green)" stroke-width="1.4"/><path d="M1.5 3.5l6.5 5 6.5-5" fill="none" stroke="var(--green)" stroke-width="1.4"/></svg>
      hello@tivaconsulting.com
    </li>
    <li>
      <svg viewBox="0 0 16 16" aria-hidden="true"><g fill="none" stroke="var(--green)" stroke-width="1.3"><circle cx="8" cy="8" r="6.3"/><ellipse cx="8" cy="8" rx="2.8" ry="6.3"/><path d="M1.7 8h12.6M3 4.5h10M3 11.5h10"/></g></svg>
      www.tivaconsulting.com
    </li>
  </ul>
</section>

<section class="card card-back" aria-label="Business card back">
  <div class="back-name">Tiva</div>
  <div class="back-sub">Consulting</div>
</section>

</body>
</html>
```